Digital One Pager for Consulting Practice

I would like the essence of the content in my ppt consolidated into a one-pager. The one-pager will mainly be sent via email as a pdf and intended to excite and invite new clients and establish the credibility of my boutique high-end consulting firm. Infographics and symbols would be a plus. The target client should view the firm as providing premeir service. The client is getting a thought partner.

Target Market(s)

Large Medical Device Manufacturer Executives, Early-Stage Medical Device Manufacturer Executives, Partners at VC Firms

Industry/Entity Type

Medical Equipment

Colors
0355a3
f37122

Requirements
Must have
• Please match the color scheme in ppt. Please use the existing logo. I am very open to better graphics on the process. My photo does not need to be on the digital flyer. Hyper link to the website and email is needed.
Nice to have
• Infographics

```html
<!DOCTYPE html>
<html lang="en">
<head>
<meta charset="utf-8">
<title>Halden Ventures – One Pager</title>
<link rel="stylesheet" href="https://fonts.googleapis.com/css2?family=Montserrat:wght@400;500;600;700&family=Tinos:wght@700&display=swap">
<style>
:root{
  --blue:#0355a3;
  --blue-bright:#1f4fe6;
  --blue-deep:#0b2fa8;
  --orange:#f37122;
  --orange-red:#f0401a;
  --ink:#111418;
  --grey-band:#e4e4e4;
  --page-bg:#7f8d8c;
  --white:#ffffff;
}
*{box-sizing:border-box;margin:0;padding:0}
html,body{width:1200px;height:968px;overflow:hidden;background:var(--page-bg)}
body{font-family:"Montserrat",Arial,sans-serif;color:var(--ink)}
.flyer{position:absolute;left:258px;top:0;width:720px;height:1018px;background:var(--white);
  transform:scale(.9509);transform-origin:0 0;overflow:hidden}
.abs{position:absolute}
.header-art,.footer-art{position:absolute;left:0;width:720px}
.header-art{top:0}
.footer-art{top:900px}
.brand{position:absolute;left:45px;top:34px;display:flex;align-items:center;gap:14px;color:var(--white);font-weight:600}
.brand-mark{width:44px;height:44px;border-radius:50%;border:4px solid var(--white)}
.brand-name{font-size:40px;letter-spacing:5px;line-height:1}
.brand-name span{display:block;font-size:19px;letter-spacing:8px;margin-top:4px}
.section-title{position:absolute;font-family:"Tinos",serif;font-weight:700;color:var(--orange-red);font-size:18px}
.section-title::after{content:"";display:block;width:54px;height:2px;background:var(--blue-bright);margin-top:2px}
.checklist{list-style:none;font-size:11.6px;line-height:14.6px}
.checklist li{position:relative;padding-left:15px}
.checklist li::before{content:"✓";position:absolute;left:0;color:var(--blue-bright);font-weight:700}
.dotlist{list-style:none;font-size:11.6px;line-height:14.6px;padding-left:15px;margin-top:5px}
.dotlist li::before{content:"•";color:var(--blue-bright);margin-right:3px}
.photo-circle{position:absolute;border-radius:50%}
.photo-main{left:389px;top:96px;width:214px;height:214px;border:4px solid var(--blue-bright);
  background:radial-gradient(circle at 45% 40%,#e9ecef,#8a939c 70%,#4a4f57)}
.photo-side{left:546px;top:200px;width:152px;height:152px;border:4px solid var(--orange-red);
  background:radial-gradient(circle at 55% 45%,#f4f5f7,#b5bcc4 75%,#6f7680)}
.diagram{position:absolute;left:55px;top:320px}
.services{position:absolute;left:385px;top:362px;width:340px;height:290px;background:var(--blue-bright);
  border:4px solid var(--blue-deep);border-right:none;border-radius:12px 0 0 12px;
  box-shadow:-2px 2px 0 #061a5c}
.services .section-title{left:14px;top:14px;color:var(--orange)}
.service{position:absolute;left:20px;display:flex;gap:24px}
.service-thumb{width:57px;height:48px;border:1px solid #fff}
.service h4{color:var(--orange);font-size:12.5px;font-weight:700;line-height:15px;margin-top:-2px}
.service ul{list-style:none;color:var(--white);font-size:11.6px;line-height:13.4px}
.service li::before{content:"✓";color:var(--orange);font-size:9px;margin-right:6px}
.provide h3{font-size:13.6px;font-weight:600;margin-bottom:3px;padding-left:15px}
.process{position:absolute;left:30px;top:678px}
.step-label{font-family:"Montserrat",Arial,sans-serif;font-size:13.5px;font-weight:600;fill:#fff}
.partners{position:absolute;left:0;top:784px;width:720px;height:55px;background:var(--grey-band);
  display:flex;align-items:center;justify-content:space-around;padding:0 14px}
.partner-badge{height:30px;border-radius:3px}
.value-title{position:absolute;left:0;top:845px;width:720px;text-align:center;font-size:27px;font-weight:700;color:var(--ink)}
.value-row{position:absolute;left:0;top:882px;width:720px;display:flex;justify-content:center;align-items:center;gap:22px;
  font-size:16px;font-weight:500;color:var(--orange-red)}
.value-dot{width:13px;height:13px;border-radius:50%;background:var(--blue-deep)}
.contact{position:absolute;left:0;top:980px;width:720px;display:flex;justify-content:center;gap:18px;
  font-size:18.5px;color:var(--white)}
.contact a{color:var(--white);text-decoration:none;display:flex;align-items:center;gap:6px}
</style>
</head>
<body>
<main class="flyer">
  <svg class="header-art" height="170" viewBox="0 0 720 170" aria-hidden="true">
    <path d="M0 0H720V112C600 80 470 90 330 118C200 142 90 138 0 122Z" fill="var(--blue-bright)"/>
    <path d="M310 117C450 88 600 76 720 118V156C640 100 480 92 310 117Z" fill="var(--orange-red)"/>
    <path d="M330 118C470 90 600 82 720 112V118C600 84 470 94 330 118Z" fill="#fff"/>
  </svg>

  <div class="brand">
    <div class="brand-mark"></div>
    <div class="brand-name">HALDEN<span>VENTURES</span></div>
  </div>

  <h2 class="section-title" style="left:30px;top:140px">Experience</h2>
  <ul class="checklist abs" style="left:30px;top:176px;width:360px">
    <li>Over a decade @FDA (Former Deputy Division Director)</li>
    <li>Expertise: Cardiovascular, Ophthalmology, General Hospital, Infection Control, Dental, Anesthesia, Respiratory</li>
    <li>Vice President Regulatory Affairs / Quality Assurance @Corvane (Fortune 150 Company)</li>
  </ul>
  <ul class="dotlist abs" style="left:30px;top:250px">
    <li>Initiated reorganization of department</li>
    <li>Led major compliance effort</li>
    <li>Successful FDA inspection (no observations)</li>
  </ul>

  <div class="photo-circle photo-main" role="img" aria-label="Photo of a team reviewing charts on a laptop"></div>
  <div class="photo-circle photo-side" role="img" aria-label="Photo of a laptop on a desk"></div>

  <h2 class="section-title" style="left:30px;top:312px">Differentiators</h2>
  <svg class="diagram" width="300" height="200" viewBox="0 0 300 200" aria-label="Leverage linked to experience, network and process">
    <line x1="37" y1="84" x2="148" y2="103" stroke="var(--blue-bright)" stroke-width="3"/>
    <line x1="148" y1="103" x2="253" y2="36" stroke="var(--blue-bright)" stroke-width="3"/>
    <line x1="148" y1="103" x2="257" y2="158" stroke="var(--blue-bright)" stroke-width="3"/>
    <circle cx="37" cy="84" r="31" fill="#c8101a" stroke="var(--blue-bright)" stroke-width="3"/>
    <circle cx="253" cy="36" r="31" fill="#1a2fc0" stroke="var(--orange-red)" stroke-width="3"/>
    <circle cx="257" cy="158" r="31" fill="#2ea81e" stroke="var(--blue-bright)" stroke-width="3"/>
    <circle cx="148" cy="103" r="56" fill="var(--orange-red)" stroke="var(--blue-bright)" stroke-width="4"/>
    <text x="37" y="88" text-anchor="middle" font-family="Montserrat,sans-serif" font-size="10.5" font-weight="500" fill="#fff">Experience</text>
    <text x="253" y="40" text-anchor="middle" font-family="Montserrat,sans-serif" font-size="10.5" font-weight="500" fill="#fff">Network</text>
    <text x="257" y="162" text-anchor="middle" font-family="Montserrat,sans-serif" font-size="10.5" font-weight="500" fill="#fff">Process</text>
    <text x="148" y="110" text-anchor="middle" font-family="Montserrat,sans-serif" font-size="20" font-weight="600" font-style="italic" fill="#fff">Leverage</text>
  </svg>

  <section class="services">
    <h2 class="section-title">Services</h2>
    <div class="service" style="top:50px">
      <div class="service-thumb" role="img" aria-label="Organization chart diagram" style="background:#f2f2f2"></div>
      <div><h4>Regulatory Strategy</h4><ul><li>RAQA Organizational Structure</li><li>Regulatory Pathway</li></ul></div>
    </div>
    <div class="service" style="top:108px">
      <div class="service-thumb" role="img" aria-label="Photo of an executive speaking" style="background:linear-gradient(135deg,#2b3f6e,#8a6b55)"></div>
      <div><h4>Interim Executive Leadership</h4><ul><li>Compliance Remediation</li><li>Accelerated Product Registration</li></ul></div>
    </div>
    <div class="service" style="top:167px">
      <div class="service-thumb" role="img" aria-label="Photo of a meeting around a table" style="background:linear-gradient(135deg,#4a3a36,#b8a79a)"></div>
      <div><h4>FDA Communications</h4><ul><li>Deficiency Response</li><li>Application Review</li></ul></div>
    </div>
    <div class="service" style="top:226px">
      <div class="service-thumb" role="img" aria-label="Photo of a training session" style="background:linear-gradient(135deg,#2a1414,#7a3a2c)"></div>
      <div><h4>Training</h4><ul><li>FDA Communication</li><li>MDR Reporting</li></ul></div>
    </div>
  </section>

  <h2 class="section-title" style="left:36px;top:503px">Experience to Provide...</h2>
  <div class="provide abs" style="left:20px;top:536px;width:370px">
    <h3>Executive Application Review</h3>
    <ul class="checklist">
      <li>Examples include: Presubmission, IDE, 510(k), 513(g), PMA, Refuse to Accept, Hold letter</li>
      <li>Troubleshooting</li>
    </ul>
    <h3 style="margin-top:4px">Strategic Advice &amp; Diligence to Investors</h3>
    <ul class="checklist">
      <li>Validate &amp; Verify Founder Milestones</li>
      <li>Diligence portfolio company Regulatory and Quality systems</li>
    </ul>
  </div>

  <h2 class="section-title" style="left:30px;top:663px">Efficient Process</h2>
  <svg class="process" width="660" height="75" viewBox="0 0 660 75" aria-label="Process: exploratory call, regulatory landscape, problem statement, review and align on deliverables">
    <defs>
      <linearGradient id="chev" x1="0" x2="1"><stop offset="0" stop-color="#2a35c8"/><stop offset="1" stop-color="#d0221a"/></linearGradient>
    </defs>
    <g fill="var(--blue-bright)">
      <rect x="0" y="18" width="143" height="36"/>
      <rect x="172" y="18" width="143" height="36"/>
      <rect x="343" y="18" width="143" height="36"/>
      <rect x="514" y="18" width="143" height="36"/>
    </g>
    <g fill="var(--blue-bright)">
      <rect x="145" y="18" width="3" height="36"/><rect x="150" y="18" width="3" height="36"/>
      <rect x="316" y="18" width="3" height="36"/><rect x="321" y="18" width="3" height="36"/>
      <rect x="487" y="18" width="3" height="36"/><rect x="492" y="18" width="3" height="36"/>
    </g>
    <path d="M156 0L187 36L156 72Z" fill="url(#chev)"/>
    <path d="M327 0L358 36L327 72Z" fill="url(#chev)"/>
    <path d="M498 0L529 36L498 72Z" fill="url(#chev)"/>
    <text class="step-label" text-anchor="middle"><tspan x="71" y="33">Exploratory</tspan><tspan x="71" y="48">Call</tspan></text>
    <text class="step-label" text-anchor="middle"><tspan x="242" y="32">Regulatory</tspan><tspan x="242" y="47">Landscape</tspan></text>
    <text class="step-label" text-anchor="middle"><tspan x="414" y="33">Problem</tspan><tspan x="414" y="48">Statement</tspan></text>
    <text class="step-label" text-anchor="middle"><tspan x="589" y="33">Review &amp; Align</tspan><tspan x="589" y="48">on Deliverables</tspan></text>
  </svg>

  <h2 class="section-title" style="left:30px;top:752px">Valued Partner Network</h2>
  <div class="partners" aria-label="Partner organisations">
    <div class="partner-badge" style="width:86px;background:#c9d2e6"></div>
    <div class="partner-badge" style="width:68px;background:#1e2a2a"></div>
    <div class="partner-badge" style="width:76px;background:#c4cbe8"></div>
    <div class="partner-badge" style="width:218px;background:#f7f7f7"></div>
    <div class="partner-badge" style="width:64px;background:var(--blue-bright)"></div>
    <div class="partner-badge" style="width:62px;background:#cfd4e8"></div>
  </div>

  <h2 class="value-title">HALDEN VENTURES VALUE</h2>
  <div class="value-row">
    <span>Extensive Experience</span><span class="value-dot"></span>
    <span>Efficient Process</span><span class="value-dot"></span>
    <span>Valued Network</span>
  </div>

  <svg class="footer-art" height="118" viewBox="0 0 720 118" aria-hidden="true">
    <path d="M0 38C140 0 280 12 400 34C520 56 620 50 720 30V118H0Z" fill="var(--orange-red)"/>
    <path d="M0 38C140 0 280 12 400 34C520 56 620 50 720 30V42C620 60 520 64 400 46C280 26 140 14 0 52Z" fill="var(--blue-bright)"/>
    <path d="M0 36C130 8 260 8 380 28C250 14 130 16 0 44Z" fill="var(--blue-bright)"/>
  </svg>
  <div class="contact">
    <a href="https://www.haldenventures.com">
      <svg width="16" height="16" viewBox="0 0 16 16" fill="none" stroke="#fff" stroke-width="1.3" aria-hidden="true"><circle cx="8" cy="8" r="7"/><ellipse cx="8" cy="8" rx="3" ry="7"/><path d="M1 8h14M2 4.5h12M2 11.5h12"/></svg>
      www.haldenventures.com</a>
    <a href="tel:2025550148">
      <svg width="17" height="17" viewBox="0 0 16 16" fill="none" stroke="#fff" stroke-width="1.3" aria-hidden="true"><circle cx="8" cy="8" r="7"/><path d="M5.2 4.5l1.4 1.6-.8 1.2c.5 1 1.3 1.8 2.3 2.3l1.2-.8 1.6 1.4-.9 1.1C7.6 11 5 8.4 4.5 5.4z"/></svg>
      202.555.0148</a>
    <a href="mailto:info@haldenventures.com">
      <svg width="18" height="14" viewBox="0 0 18 14" fill="none" stroke="#fff" stroke-width="1.3" aria-hidden="true"><rect x="1" y="1" width="16" height="12"/><path d="M1 1l8 7 8-7"/></svg>
      info@haldenventures.com</a>
  </div>
</main>
</body>
</html>
```